4 Month Comparison Sales Promotion Infographic

HI ALL - SEEMS TO BE SOME CONFUSION RE: JANUARY - JANUARY HAS NO EXTRA BENEFITS, SAME AS DECEMBER. THE DIFFERENCE BETWEEN DECEMBER AND JANUARY IS ONLY PRICE. THE ONLY MONTHS WITH EXTRA BENEFITS ARE OCTOBER AND NOVEMBER. THANK YOU!

Project needs to be completed in 24 hours. Need it for tomorrow by 3pm EST.

Project Overview: We are developing an infographic to effectively present our U.S. Federal Contracting consulting package. This package is currently available for $21,000, despite its components having a retail value of $35,750. Beginning January 1st, 2025, the package price will rise by 25% to $28,600.

Goal of the Project: The primary objective is to motivate customers to purchase the package in October or November, before the upcoming price increase. This infographic will strategically illustrate the incremental value gained from making an earlier purchase.

Target Audience: The focus is on U.S. business owners who typically postpone significant investments during the holiday season, from November 15th to January 1st. The infographic is designed to encourage these customers to consider the benefits of acting sooner rather than later.

Visual Concept: The infographic will employ a "compare/contrast" style to demonstrate the following:

October: Best Value — Achieve the highest total package value of $50,750 at the lowest cost of $21,000.
November: Great Value — Still substantial, with a package value of $41,600 available for the same cost of $21,000.
December: Really Good Value — Standard retail value of $35,750 obtainable for $21,000.
January: Good Deal — Same retail value of $35,750, but at the increased price of $28,600. NO ADDITIONAL BENEFITS (SAME AS DECEMBER)
Key Features:

Clear and compelling visuals that contrast cost versus value for each month.
Design that aligns with your brand’s visual identity, enhancing message delivery through an engaging, on-brand presentation.
A strong emphasis on the superior value of purchasing in October or November over January to highlight the financial wisdom in early decision-making.

This is all displayed in images that we've shared, along with the associated benefits.

Branding Information
Website: www.tarvelmoor.com
Colors:
Primary Color: #042756 (Dark Blue)
Accent Color: #D96F1F (Orange)
Fonts:
Heading Font:
Font Family: Manrope
Font Size: 68px
Line Height: 74.8px
Text Alignment: Left (Start)
Letter Spacing: -1.36px
Body Font:
Font Family: Manrope
Font Size: 18px
Line Height: 32.4px
Letter Spacing: -0.36px

Target Market(s)

Business owners interested in federal contracting

Industry/Entity Type

B2B, but focused on B2B (Business to Government)

Font styles to use
Other font styles liked:
• Manrope (Heading and Body)

Colors
0054AA
0677BA
7BADD7
CADEEF
E8F1F8
EE7325
F08F49
F5BC92
FAE3D3
FDF4ED

Requirements
Must have
• Need to clearly represent the 4 month window, costs, and benefits and difference in cost vs. value. Clearly defined information that highlights value of purchasing in October vs. waiting for later months.
Nice to have
• Unique icons and/or designs that are outside the box and really wow the client.

```html
<!DOCTYPE html>
<html lang="en">
<head>
<meta charset="utf-8">
<title>End of Year Promotion – Tarvelmoor</title>
<link href="https://fonts.googleapis.com/css2?family=Manrope:wght@400;500;600;700;800&display=swap" rel="stylesheet">
<style>
  :root {
    --night: #0a0826;
    --indigo: #1e1a6b;
    --violet: #3a2fa8;
    --card-blue: #3b3e8e;
    --card-blue-dark: #2c2f78;
    --amber: #f3a73a;
    --amber-dark: #d98a22;
    --orange: #f08a3a;
    --white: #ffffff;
    --ring: #c9c9d6;
    --cyan: #1fe0f0;
    --ink: #26245e;
  }
  * { box-sizing: border-box; margin: 0; padding: 0; }
  html, body { width: 877px; height: 1200px; overflow: hidden; }
  body {
    font-family: "Manrope", sans-serif;
    color: var(--white);
    background:
      radial-gradient(ellipse 480px 380px at 10% 5%, rgba(72,58,200,.55), transparent 70%),
      radial-gradient(ellipse 420px 360px at 100% 55%, rgba(60,48,180,.45), transparent 70%),
      radial-gradient(ellipse 500px 300px at 60% 100%, rgba(70,55,190,.45), transparent 70%),
      var(--night);
    position: relative;
  }
  .headline {
    position: absolute; left: 0; width: 877px; text-align: center;
    font-weight: 700; letter-spacing: -1.2px; line-height: 1;
  }
  .headline--top { top: 64px; font-size: 72px; }
  .headline--accent { top: 140px; font-size: 76px; color: var(--orange); }
  .subline {
    position: absolute; top: 220px; left: 60px; width: 800px; height: 34px;
    background: linear-gradient(90deg, transparent, rgba(80,80,170,.45) 20%, rgba(80,80,170,.45) 80%, transparent);
    text-align: center; font-size: 27px; line-height: 34px; font-weight: 400; letter-spacing: -.5px;
  }
  .promo-pill {
    position: absolute; top: 278px; left: 255px; width: 334px; height: 41px;
    border: 1.5px solid #35b8d8; border-radius: 21px;
    text-align: center; font-size: 21px; line-height: 39px; font-weight: 800; letter-spacing: 1px;
  }
  .connector { position: absolute; border: 2px solid var(--amber); }
  .connector--left { left: 144px; top: 429px; width: 40px; height: 197px; border-right: none; }
  .connector--right { left: 778px; top: 822px; width: 40px; height: 171px; border-left: none; }

  .tier-card {
    position: absolute; height: 100px;
    display: flex; align-items: center; justify-content: center; text-align: center;
    font-size: 18px; line-height: 26px; font-weight: 500; letter-spacing: -.2px;
  }
  .tier-card::after {
    content: ""; position: absolute; left: 20px; right: 8px; bottom: -10px; height: 20px;
    background: var(--white); z-index: -1; border-radius: 0 0 60px 60px;
  }
  .tier-card--blue { left: 287px; width: 491px; background: var(--card-blue); border-radius: 0 50px 50px 0; padding-left: 30px; }
  .tier-card--blue::before {
    content: ""; position: absolute; left: 0; top: -9px; width: 80px; height: 109px;
    background: var(--card-blue-dark); z-index: -1;
  }
  .tier-card--amber { left: 177px; width: 476px; background: var(--amber); border-radius: 50px 0 0 50px; padding-right: 30px; }
  .tier-card--amber::after { left: 8px; right: 20px; border-radius: 0 0 0 60px; }
  .tier-card--amber::before {
    content: ""; position: absolute; right: 0; top: -28px; width: 80px; height: 128px;
    background: var(--amber-dark); z-index: -1;
  }
  .tier-card { z-index: 1; }

  .tier-badge {
    position: absolute; height: 26px; display: flex; border-radius: 13px; overflow: hidden;
    font-size: 19px; font-weight: 700; line-height: 26px; z-index: 2;
  }
  .tier-badge span { padding: 0 8px; }
  .tier-badge--blue { background: var(--card-blue); }
  .tier-badge--blue .month { background: var(--amber); color: var(--ink); border-radius: 13px; }
  .tier-badge--amber { background: var(--amber); }
  .tier-badge--amber .month { background: var(--card-blue); color: var(--amber); border-radius: 13px; }
  .tier-badge--amber .label { color: var(--white); }
  .tier-badge--ink .label { color: var(--ink); }

  .trend-icon { position: absolute; width: 138px; height: 138px; z-index: 3; }

  .footer-phone { position: absolute; left: 203px; top: 1138px; font-size: 18px; font-weight: 500; }
  .footer-divider { position: absolute; top: 1123px; width: 2px; height: 50px; background: var(--amber); }
  .footer-brand { position: absolute; left: 380px; top: 1138px; width: 100px; text-align: center; font-size: 15px; font-weight: 700; }
  .footer-contact { position: absolute; left: 530px; font-size: 8.5px; font-weight: 600; display: flex; align-items: center; gap: 5px; }
  .footer-web { position: absolute; top: 1183px; left: 0; width: 877px; text-align: center; font-size: 10px; letter-spacing: 10px; font-weight: 500; }
</style>
</head>
<body>
  <h1 class="headline headline--top">Maximize Savings</h1>
  <h2 class="headline headline--accent">Before the Price Rises!</h2>
  <p class="subline">Lock in Your Federal Contracting Advantage Now!</p>
  <div class="promo-pill">END OF YEAR PROMOTION</div>

  <div class="connector connector--left"></div>
  <div class="connector connector--right"></div>

  <!-- October -->
  <div class="tier-badge tier-badge--blue" style="left:369px;top:377px;"><span class="month">OCTOBER</span><span class="label">BEST VALUE</span></div>
  <div class="tier-card tier-card--blue" style="top:405px;">Achieve the highest total package value of<br>$50,750 at the lowest cost of $21,000.</div>
  <svg class="trend-icon" style="left:189px;top:356px;" viewBox="0 0 138 138">
    <circle cx="69" cy="69" r="66" fill="var(--card-blue)" stroke="var(--ring)" stroke-width="4"/>
    <polyline points="36,26 58,62 66,54 90,100" fill="none" stroke="var(--cyan)" stroke-width="6"/>
    <polygon points="80,100 98,96 96,114" fill="var(--cyan)"/>
  </svg>

  <!-- November -->
  <div class="tier-badge tier-badge--amber" style="left:299px;top:557px;"><span class="month">NOVEMBER</span><span class="label">GREAT VALUE</span></div>
  <div class="tier-card tier-card--amber" style="top:586px;">Still substantial, with a package value of<br>$41,600 available for the same cost of $21,000</div>
  <svg class="trend-icon" style="left:614px;top:544px;" viewBox="0 0 138 138">
    <circle cx="69" cy="69" r="66" fill="var(--amber)" stroke="var(--ring)" stroke-width="4"/>
    <polyline points="30,104 56,78 64,86 104,34" fill="none" stroke="var(--cyan)" stroke-width="6"/>
    <polygon points="96,32 112,26 108,44" fill="var(--cyan)"/>
  </svg>

  <!-- December -->
  <div class="tier-badge tier-badge--blue" style="left:370px;top:744px;"><span class="month">DECEMBER</span><span class="label">REALLY GOOD VALUE</span></div>
  <div class="tier-card tier-card--blue" style="top:773px;">Standard retail value of $35,750<br>obtainable for $21,000.</div>
  <svg class="trend-icon" style="left:189px;top:724px;" viewBox="0 0 138 138">
    <circle cx="69" cy="69" r="66" fill="var(--card-blue)" stroke="var(--ring)" stroke-width="4"/>
    <polyline points="36,26 58,62 66,54 90,100" fill="none" stroke="var(--cyan)" stroke-width="6"/>
    <polygon points="80,100 98,96 96,114" fill="var(--cyan)"/>
  </svg>

  <!-- January -->
  <div class="tier-badge tier-badge--amber tier-badge--ink" style="left:301px;top:925px;"><span class="month">JANUARY</span><span class="label">GOOD DEAL</span></div>
  <div class="tier-card tier-card--amber" style="top:955px;">Same retail value of $35,750, but at<br>the increased price of $28,600</div>
  <svg class="trend-icon" style="left:614px;top:912px;" viewBox="0 0 138 138">
    <circle cx="69" cy="69" r="66" fill="var(--amber)" stroke="var(--ring)" stroke-width="4"/>
    <polyline points="30,104 56,78 64,86 104,34" fill="none" stroke="var(--cyan)" stroke-width="6"/>
    <polygon points="96,32 112,26 108,44" fill="var(--cyan)"/>
  </svg>

  <footer>
    <div class="footer-phone">555-014-2276</div>
    <div class="footer-divider" style="left:346px;"></div>
    <div class="footer-brand">Tarvelmoor</div>
    <div class="footer-divider" style="left:506px;"></div>
    <div class="footer-contact" style="top:1131px;">
      <svg width="10" height="8" viewBox="0 0 10 8"><rect x=".5" y=".5" width="9" height="7" fill="none" stroke="#fff"/><polyline points=".5,.5 5,4.5 9.5,.5" fill="none" stroke="#fff"/></svg>
      hello@tarvelmoor.com
    </div>
    <div class="footer-contact" style="top:1153px;">
      <svg width="8" height="11" viewBox="0 0 8 11"><path d="M4 10.5 C1 6.5 .5 5 .5 4 a3.5 3.5 0 0 1 7 0 c0 1-.5 2.5-3.5 6.5z" fill="none" stroke="#fff"/><circle cx="4" cy="4" r="1.2" fill="#fff"/></svg>
      218 Alder Row, Fenwick, NV 89000
    </div>
    <div class="footer-web">WWW.TARVELMOOR.COM</div>
  </footer>
</body>
</html>
```